WebSite for Online Insurance Company

We will establish a web portal which gives service for online insurance service
like https://www.coverlantern.com/ but we need more fresh desing one of our competitor in turkey is https://www.korunmak.net/ our main target is car insurance .
We are really looking for higly qualified senior designers who will make all desing process of this company's requirements both for web site/mobile and printed materials. but right now we look for first for website. We attached the logo for our velora but website name has changed as veloraguvence.com

We'll have one main page and 4-5 inner pages and processses for getting order and processing.

we have explained above also our logo needs to be modified needs to be removed the velora.cab address from there.
our turkish competitor is www.korunmak.net but we liked the styels of https://www.qrv.com.sg
https://www.pebblemarkcover.co.nz/ and also https://www.layoutbarrow.com/demo/73162.html
We do not have a spesific idea about what we want but our major working area will be car insurance so the name of the company is VELORA and our domain is veloraguvence.com.
If you want us to be sure about your desing quality and time process, we kindly request from you a great homepage

```html
<!DOCTYPE html>
<html lang="en">
<head>
<meta charset="utf-8">
<title>Velora Güvence — Online Car Insurance</title>
<link href="https://fonts.googleapis.com/css2?family=Roboto:wght@400;500;700;900&display=swap" rel="stylesheet">
<style>
:root{
  --yellow:#fdd22a;
  --yellow-deep:#f3c315;
  --ink:#1c1c1c;
  --ink-soft:#2a2a2a;
  --grey-bg:#efefef;
  --muted:#8a8a8a;
  --text:#333;
  --white:#fff;
  --green:#3cad3c;
}
*{box-sizing:border-box;margin:0;padding:0}
html,body{width:1200px;height:5365px;overflow:hidden}
body{font-family:'Roboto',Arial,sans-serif;color:var(--text);background:var(--white);position:relative}
section,header,footer,nav{position:absolute;left:0;width:1200px}
.center{text-align:center}
.btn{display:inline-flex;align-items:center;gap:14px;background:var(--yellow);color:var(--ink);font-weight:700;text-transform:uppercase;justify-content:center;letter-spacing:.2px}
.btn .arr{width:24px;height:24px;border-radius:50%;background:var(--ink);display:inline-flex;align-items:center;justify-content:center}
.btn .arr svg{width:12px;height:12px}
.sec-title{font-size:31px;font-weight:700;color:var(--ink)}
.sec-sub{font-size:14px;color:var(--muted)}
.ph{position:absolute}

/* top bar */
.topbar{top:0;height:25px;background:var(--ink);color:#ddd;font-size:10px}
.topbar .phone{position:absolute;left:120px;top:0;height:25px;background:var(--yellow);color:var(--ink);font-weight:700;padding:0 10px;display:flex;align-items:center;gap:5px}
.topbar .info{position:absolute;left:255px;top:0;height:25px;display:flex;align-items:center;gap:22px}
.topbar .user{position:absolute;right:118px;top:0;height:25px;display:flex;align-items:center;gap:10px}
.topbar .login{background:var(--yellow);color:var(--ink);font-weight:700;padding:0 10px;height:25px;display:flex;align-items:center}

/* header */
.masthead{top:25px;height:90px;background:var(--white)}
.brand{position:absolute;left:120px;top:24px;display:flex;align-items:center;gap:8px}
.brand .mark{width:30px;height:30px;background:var(--ink)}
.brand .name{font-size:38px;font-weight:900;color:var(--yellow-deep);letter-spacing:1px}
.quote-btn{position:absolute;left:960px;top:30px;height:34px;padding:0 4px 0 16px;border-radius:17px;font-size:11px;text-transform:none}
.mainnav{top:115px;height:35px}
.mainnav ul{position:absolute;left:119px;width:969px;height:35px;background:var(--ink);list-style:none;display:flex;font-size:11px;font-weight:500;color:#fff}
.mainnav li{padding:0 16px;display:flex;align-items:center}
.mainnav li.active{background:#3a3a3a}

/* hero */
.hero{top:150px;height:481px;background:linear-gradient(90deg,#e7dccd 0%,#f4ece0 35%,#f2ebe2 60%,#e6ddd2 100%);overflow:hidden}
.hero .visual{inset:0;position:absolute;background:radial-gradient(ellipse at 40% 20%,rgba(214,180,140,.55),transparent 55%),radial-gradient(ellipse at 85% 80%,rgba(200,60,60,.35),transparent 30%)}
.hero h1{position:absolute;top:160px;width:100%;text-align:center;font-size:60px;font-weight:900;color:var(--ink);letter-spacing:-1px}
.hero h2{position:absolute;top:228px;width:100%;text-align:center;font-size:23px;font-weight:500;color:var(--ink)}
.hero p{position:absolute;top:264px;left:265px;width:670px;text-align:center;font-size:11.5px;font-weight:700;color:var(--ink);line-height:1.3}
.hero .btn{position:absolute;left:470px;top:312px;width:262px;height:50px;font-size:16px}
.hero .dots{position:absolute;top:435px;left:0;width:100%;display:flex;justify-content:center;gap:6px}
.dots i{width:8px;height:8px;border-radius:50%;background:#555;display:block}
.dots i.on{background:var(--yellow-deep)}
.hero .dots{background:none}
.hero .dots-wrap{position:absolute;top:427px;left:532px;width:136px;height:24px;background:rgba(0,0,0,.15)}

/* products */
.products{top:631px;height:587px}
.products .sec-title{position:absolute;top:68px;width:100%;text-align:center;font-size:34px}
.products .lead{position:absolute;top:114px;width:100%;text-align:center;font-size:19px;font-weight:500;color:#444}
.products .copy{position:absolute;top:143px;left:330px;width:540px;text-align:center;font-size:11px;color:#555;line-height:1.35}
.tiles{position:absolute;top:200px;left:119px;width:962px;display:grid;grid-template-columns:repeat(6,150px);gap:19px 12.4px}
.tile{height:90px;background:var(--ink);color:#fff;font-size:9.5px;font-weight:700;display:flex;flex-direction:column;align-items:center;justify-content:center;gap:10px;text-transform:uppercase}
.tile svg{width:28px;height:28px}
.tile.active{background:var(--yellow);color:var(--ink);outline:3px solid var(--ink);outline-offset:-6px}
.products .btn{position:absolute;left:469px;top:448px;width:262px;height:56px;font-size:16px}

/* why */
.why{top:1218px;height:642px;background:linear-gradient(160deg,#5e5c55 0%,#45433e 45%,#3a3935 100%);color:#fff}
.why .sec-title{position:absolute;top:86px;width:100%;text-align:center;color:#fff;font-size:26px}
.why .sec-sub{position:absolute;top:122px;width:100%;text-align:center;color:#ddd;font-size:17px}
.feature{position:absolute;width:300px;display:flex;gap:18px}
.feature .ring{flex:none;width:112px;height:112px;border-radius:50%;background:var(--yellow);display:flex;align-items:center;justify-content:center}
.feature .ring span{width:90px;height:90px;border-radius:50%;background:#fff;display:flex;align-items:center;justify-content:center}
.feature .ring svg{width:44px;height:44px}
.feature h3{font-size:13px;font-weight:500;line-height:1.15;margin-top:22px}
.feature p{font-size:9px;color:#ccc;margin-top:6px;line-height:1.25}
.why .btn{position:absolute;left:467px;top:517px;width:264px;height:57px;background:#fff;font-size:16px}
.why .btn .arr{background:var(--yellow)}

/* how */
.how{top:1860px;height:404px}
.how .sec-title{position:absolute;top:60px;width:100%;text-align:center;font-size:27px}
.how .sec-sub{position:absolute;top:100px;left:160px;width:880px;text-align:center;font-size:11px;line-height:1.35;color:#999}
.step{position:absolute;top:152px;width:300px;height:119px;background:#fff;box-shadow:0 2px 8px rgba(0,0,0,.14);display:flex;gap:18px;align-items:flex-start;padding:28px 18px}
.step .ic{flex:none;width:56px;height:56px;border-radius:50%;background:var(--yellow);display:flex;align-items:center;justify-content:center}
.step .ic svg{width:26px;height:26px}
.step h4{font-size:12px;font-weight:700;color:var(--ink);text-transform:uppercase}
.step p{font-size:11px;color:#888;line-height:1.3;margin-top:6px}
.how .btn{position:absolute;left:483px;top:302px;width:234px;height:48px;font-size:15px}

/* testimonials */
.reviews{top:2264px;height:454px;background:var(--grey-bg)}
.reviews .sec-title{position:absolute;top:62px;width:100%;text-align:center;font-size:29px}
.reviews .rated{position:absolute;top:103px;width:100%;text-align:center;font-size:11px;color:#777}
.reviews .rated b{color:var(--ink)}
.review{position:absolute;top:153px;width:300px;height:183px;background:#fff;box-shadow:0 1px 4px rgba(0,0,0,.1);padding:20px 18px}
.review h5{font-size:13px;font-weight:500;color:var(--ink);display:flex;align-items:center;gap:8px}
.review h5 i{width:18px;height:18px;border-radius:50%;background:#ddd;display:block}
.review p{font-size:11px;color:#666;line-height:1.3;margin-top:8px}
.review .who{position:absolute;left:18px;bottom:18px;display:flex;gap:8px;align-items:center;font-size:8.5px;color:#555;line-height:1.2}
.review .who .av{width:24px;height:24px;border-radius:50%;background:#c8c2b8}
.review .stars{position:absolute;right:18px;bottom:22px;display:flex;gap:2px}
.review .stars i{width:15px;height:15px;background:var(--green);display:block}
.reviews .nav-arr{position:absolute;top:232px;width:30px;height:60px}
.reviews .dots{position:absolute;top:380px;width:100%;display:flex;justify-content:center;gap:6px}
.reviews .dots i{background:#999}
.reviews .dots i.on{background:var(--yellow-deep)}

/* banner */
.promo{top:2718px;height:294px;background:linear-gradient(90deg,#ece5dc 0%,#dcd1c4 40%,#5a5853 62%,#3a3936 100%)}
.promo .photo{position:absolute;left:0;top:0;width:729px;height:294px;background:radial-gradient(ellipse at 25% 45%,#d7b99b 0%,transparent 45%),radial-gradient(ellipse at 55% 60%,#f0c41f 0%,transparent 25%)}
.promo .panel{position:absolute;left:729px;top:0;width:471px;height:294px;background:rgba(30,30,30,.7)}
.promo .kicker{position:absolute;left:752px;top:50px;font-size:11px;color:#fff;font-weight:500}
.promo h3{position:absolute;left:752px;top:72px;width:300px;font-size:22px;font-weight:700;color:var(--yellow);line-height:1.08}
.promo ul{position:absolute;left:752px;top:137px;list-style:none;font-size:11px;color:#fff;line-height:1.65}
.promo ul li::before{content:"";display:inline-block;width:7px;height:7px;border-radius:50%;background:#fff;margin-right:8px}
.promo .btn{position:absolute;left:748px;top:212px;width:175px;height:36px;font-size:11px}
.promo .seal{position:absolute;left:1027px;top:118px;width:100px;height:100px;border-radius:50%;background:var(--yellow);border:6px solid var(--ink)}

/* companies */
.partners{top:3012px;height:608px}
.partners .sec-title{position:absolute;top:80px;width:100%;text-align:center;font-size:27px}
.partners .sec-sub{position:absolute;top:120px;width:100%;text-align:center;font-size:11px;color:#666}
.logos{position:absolute;top:156px;left:110px;display:grid;grid-template-columns:repeat(6,142px);gap:17px 26px}
.logos span{height:58px;background:#fff;box-shadow:0 1px 5px rgba(0,0,0,.16);display:flex;align-items:center;justify-content:center;font-size:13px;font-weight:700;color:#2f4f8f;text-align:center}
.partners .btn{position:absolute;left:444px;top:490px;width:310px;height:44px;font-size:12px;text-transform:none}

/* stats */
.stats{top:3620px;height:375px;background:linear-gradient(160deg,#4e4c47 0%,#3b3a37 55%,#2e2d2b 100%);color:#fff}
.stats .sec-title{position:absolute;top:72px;width:100%;text-align:center;color:#fff;font-size:27px}
.stats .sec-sub{position:absolute;top:108px;left:340px;width:520px;text-align:center;color:#eee;font-size:11px;font-weight:700;line-height:1.3}
.stat{position:absolute;top:163px;width:160px;text-align:center}
.stat .c{width:84px;height:84px;border-radius:50%;background:var(--yellow);margin:0 auto;display:flex;align-items:center;justify-content:center}
.stat .c svg{width:38px;height:38px}
.stat b{display:block;font-size:44px;font-weight:700;margin-top:10px}
.stat small{font-size:9px;text-transform:uppercase;color:#ddd}

/* articles */
.articles{top:3995px;height:852px}
.articles .sec-title{position:absolute;top:68px;width:100%;text-align:center;font-size:27px}
.posts{position:absolute;top:125px;left:119px;display:grid;grid-template-columns:repeat(4,234px);gap:18px 10px}
.post{height:260px;background:#fff;box-shadow:0 1px 5px rgba(0,0,0,.15);position:relative}
.post .img{height:140px}
.post .tag{font-size:7.5px;font-weight:700;color:#b38a00;text-transform:uppercase;margin:8px 10px 0}
.post h6{font-size:9.5px;font-weight:700;color:var(--ink);margin:3px 10px 0}
.post .meta{font-size:7px;color:#999;margin:2px 10px 0}
.post p{font-size:8.5px;color:#666;line-height:1.25;margin:5px 10px 0}
.post .go{position:absolute;right:8px;bottom:8px;width:16px;height:16px;border-radius:50%;background:var(--yellow)}
.articles .more{position:absolute;left:506px;top:702px;width:188px;height:38px;background:var(--ink);color:#fff;font-size:12px;font-weight:700;display:flex;align-items:center;justify-content:center;gap:14px}
.articles .more .arr{width:22px;height:22px;border-radius:50%;background:var(--yellow)}
.chat{position:absolute;left:854px;top:817px;width:225px;height:33px;background:var(--green);color:#fff;font-size:11px;font-weight:700;display:flex;align-items:center;justify-content:center;gap:8px}

/* call bar */
.callbar{top:4847px;height:79px;background:var(--yellow);display:flex;align-items:center;justify-content:center;font-size:27px;font-weight:700;color:var(--ink)}

/* footer */
.site-foot{top:4926px;height:344px;background:#232323;color:#aaa}
.site-foot .brand{left:119px;top:38px}
.site-foot .brand .name{font-size:32px}
.site-foot .about{position:absolute;left:119px;top:92px;width:230px;font-size:9px;line-height:1.35;color:#999}
.site-foot .legal{position:absolute;left:119px;top:170px;font-size:8px;color:#888}
.socials{position:absolute;left:119px;top:176px;display:flex;gap:14px}
.socials i{width:34px;height:34px;border-radius:50%;background:var(--yellow);display:block}
.fcol{position:absolute;top:44px;font-size:9px;line-height:1.9;color:#999}
.fcol h5{font-size:11px;color:#fff;font-weight:700;text-transform:uppercase;margin-bottom:12px}
.fcol .row{display:flex;gap:8px;align-items:flex-start;line-height:1.35;margin-bottom:8px}
.fcol .row svg{flex:none;width:14px;height:14px}
.subscribe{position:absolute;left:840px;top:234px}
.subscribe h5{font-size:11px;color:#fff;font-weight:700;text-transform:uppercase}
.subscribe .field{margin-top:14px;width:240px;height:38px;background:#fff;display:flex}
.subscribe .field span{flex:1;font-size:9px;color:#777;padding:13px 10px}
.subscribe .field b{width:36px;background:var(--yellow);display:flex;align-items:center;justify-content:center}
.baseline{top:5270px;height:95px;background:#1a1a1a;color:#888;font-size:9px;text-align:center;padding-top:38px;line-height:1.8}
</style>
</head>
<body>

<svg width="0" height="0" style="position:absolute">
  <defs>
    <symbol id="i-arrow" viewBox="0 0 12 12"><path d="M3 2l5 4-5 4" fill="none" stroke="currentColor" stroke-width="2"/></symbol>
    <symbol id="i-car" viewBox="0 0 32 32"><path d="M5 20l3-8h16l3 8v6H5z" fill="currentColor"/><circle cx="10" cy="26" r="3" fill="currentColor"/><circle cx="22" cy="26" r="3" fill="currentColor"/></symbol>
    <symbol id="i-sun" viewBox="0 0 32 32"><circle cx="16" cy="16" r="6" fill="currentColor"/><path d="M16 3v5M16 24v5M3 16h5M24 16h5M7 7l3 3M22 22l3 3M25 7l-3 3M7 25l3-3" stroke="currentColor" stroke-width="2"/></symbol>
    <symbol id="i-kit" viewBox="0 0 32 32"><rect x="4" y="9" width="24" height="18" rx="2" fill="currentColor"/><rect x="12" y="5" width="8" height="5" fill="none" stroke="currentColor" stroke-width="2"/><path d="M16 13v10M11 18h10" stroke="#1c1c1c" stroke-width="3"/></symbol>
    <symbol id="i-bars" viewBox="0 0 32 32"><path d="M4 28h24" stroke="currentColor" stroke-width="2"/><rect x="6" y="18" width="4" height="9" fill="currentColor"/><rect x="13" y="12" width="4" height="15" fill="currentColor"/><rect x="20" y="6" width="4" height="21" fill="currentColor"/></symbol>
    <symbol id="i-bike" viewBox="0 0 32 32"><circle cx="8" cy="21" r="5" fill="none" stroke="currentColor" stroke-width="2.5"/><circle cx="24" cy="21" r="5" fill="none" stroke="currentColor" stroke-width="2.5"/><path d="M8 21l6-8h7l3 8M12 13h5" stroke="currentColor" stroke-width="2.5" fill="none"/></symbol>
    <symbol id="i-plane" viewBox="0 0 32 32"><path d="M2 17l28-3-28-3 3 3zM14 14l-4-9h3l7 9zM14 17l-4 9h3l7-9z" fill="currentColor"/></symbol>
    <symbol id="i-people" viewBox="0 0 32 32"><circle cx="10" cy="8" r="4" fill="currentColor"/><circle cx="22" cy="8" r="4" fill="currentColor"/><path d="M5 28V15h10v13zM17 28V15h10v13z" fill="currentColor"/></symbol>
    <symbol id="i-coin" viewBox="0 0 32 32"><circle cx="16" cy="16" r="12" fill="none" stroke="currentColor" stroke-width="2.5"/><circle cx="16" cy="16" r="6" fill="currentColor"/></symbol>
    <symbol id="i-home" viewBox="0 0 32 32"><path d="M4 16L16 5l12 11h-4v11H8V16z" fill="currentColor"/></symbol>
    <symbol id="i-hand" viewBox="0 0 32 32"><path d="M3 22h8l6 3 10-5-2-2-7 2-4-2H3z" fill="currentColor"/><circle cx="20" cy="10" r="5" fill="currentColor"/></symbol>
    <symbol id="i-doc" viewBox="0 0 32 32"><rect x="7" y="4" width="18" height="24" rx="2" fill="none" stroke="currentColor" stroke-width="2.5"/><path d="M11 11h10M11 16h10M11 21h7" stroke="currentColor" stroke-width="2"/></symbol>
    <symbol id="i-screen" viewBox="0 0 32 32"><rect x="4" y="6" width="24" height="16" rx="1" fill="none" stroke="currentColor" stroke-width="2.5"/><path d="M12 27h8M16 22v5M8 18l5-5 4 3 6-6" stroke="currentColor" stroke-width="2" fill="none"/></symbol>
    <symbol id="i-user" viewBox="0 0 32 32"><circle cx="16" cy="10" r="6" fill="currentColor"/><path d="M5 28c0-7 5-10 11-10s11 3 11 10z" fill="currentColor"/></symbol>
    <symbol id="i-cal" viewBox="0 0 32 32"><rect x="4" y="7" width="24" height="21" rx="2" fill="none" stroke="currentColor" stroke-width="2.5"/><path d="M4 13h24M10 4v6M22 4v6" stroke="currentColor" stroke-width="2.5"/></symbol>
    <symbol id="i-pin" viewBox="0 0 16 16"><path d="M8 1a5 5 0 0 1 5 5c0 4-5 9-5 9S3 10 3 6a5 5 0 0 1 5-5z" fill="currentColor"/><circle cx="8" cy="6" r="2" fill="#232323"/></symbol>
    <symbol id="i-phone" viewBox="0 0 16 16"><path d="M4 1h3l1 4-2 1c1 2 2 3 4 4l1-2 4 1v3c0 1-1 2-2 2C7 14 2 9 2 3c0-1 1-2 2-2z" fill="currentColor"/></symbol>
    <symbol id="i-mail" viewBox="0 0 16 16"><rect x="1" y="3" width="14" height="10" fill="none" stroke="currentColor" stroke-width="1.5"/><path d="M1 3l7 6 7-6" fill="none" stroke="currentColor" stroke-width="1.5"/></symbol>
    <symbol id="i-clock" viewBox="0 0 16 16"><circle cx="8" cy="8" r="6.5" fill="none" stroke="currentColor" stroke-width="1.5"/><path d="M8 4v4l3 2" stroke="currentColor" stroke-width="1.5" fill="none"/></symbol>
  </defs>
</svg>

<div class="topbar" style="position:absolute;left:0;width:1200px">
  <div class="phone"><svg width="10" height="10"><use href="#i-phone"/></svg>1-800-555-0142</div>
  <div class="info"><span>214 Kestane Sk #12, Istanbul, 34410</span><span>Mon-Sat : 08.00 am - 06.00 pm</span></div>
  <div class="user"><span>New User</span><span class="login">Member login</span></div>
</div>

<header class="masthead">
  <div class="brand"><span class="mark"></span><span class="name">VELORA</span></div>
  <a class="btn quote-btn">Get a Quote <span class="arr" style="color:#fff"><svg><use href="#i-arrow"/></svg></span></a>
</header>

<nav class="mainnav">
  <ul>
    <li class="active">Home</li><li>Products ▾</li><li>Help</li><li>Claims</li><li>About Velora</li><li>Testimonials</li><li>Blog</li><li>Contactus</li>
  </ul>
</nav>

<section class="hero">
  <div class="visual" role="img" aria-label="Photo of a smiling family at home with a red sports car in the foreground"></div>
  <h1>simple. reliable. direct.</h1>
  <h2>It is now time for a more Affordable Car Insurance.</h2>
  <p>Your monthly car repayment will be lowered when you refinance your vehicle, with the benefits of a lower interest rate too. Your monthly car repayment will be lowered when your benefits of a lower interest rate too.</p>
  <a class="btn">Apply Online Now <span class="arr" style="color:#fff"><svg><use href="#i-arrow"/></svg></span></a>
  <div class="dots-wrap"></div>
  <div class="dots"><i class="on"></i><i></i><i></i><i></i><i></i><i></i><i></i><i></i></div>
</section>

<section class="products">
  <h2 class="sec-title">Trade Smart Insurance.</h2>
  <div class="lead">Committed to making it easy to insure your home, car and contents.</div>
  <p class="copy">We provide Turkey's first online insurance broker since 2001, as more than 3 million people, 10 million of insurance on offer. With our experienced staff, we are with you 24/7!</p>
  <div class="tiles">
    <div class="tile active"><svg><use href="#i-car"/></svg>Car</div>
    <div class="tile" style="color:#fff"><svg style="color:var(--yellow)"><use href="#i-sun"/></svg>Term Life</div>
    <div class="tile"><svg style="color:var(--yellow)"><use href="#i-kit"/></svg>International Health</div>
    <div class="tile"><svg style="color:var(--yellow)"><use href="#i-bars"/></svg>Investment Plan</div>
    <div class="tile"><svg style="color:var(--yellow)"><use href="#i-bike"/></svg>Two Wealer</div>
    <div class="tile"><svg style="color:var(--yellow)"><use href="#i-plane"/></svg>Travel</div>
    <div class="tile"><svg style="color:var(--yellow)"><use href="#i-car"/></svg>Commercial Car</div>
    <div class="tile"><svg style="color:var(--yellow)"><use href="#i-people"/></svg>Child Plans</div>
    <div class="tile"><svg style="color:var(--yellow)"><use href="#i-kit"/></svg>Return of Premium</div>
    <div class="tile"><svg style="color:var(--yellow)"><use href="#i-coin"/></svg>Guarendeet Return</div>
    <div class="tile"><svg style="color:var(--yellow)"><use href="#i-hand"/></svg>Investment</div>
    <div class="tile"><svg style="color:var(--yellow)"><use href="#i-home"/></svg>Home Insurance</div>
  </div>
  <a class="btn">Apply Online Now <span class="arr" style="color:#fff"><svg><use href="#i-arrow"/></svg></span></a>
</section>

<section class="why" role="region" aria-label="Why choose Velora, over a dimmed photo of a person on the road">
  <h2 class="sec-title">Why Choose Veloraguvence Now ?</h2>
  <div class="sec-sub">we've made insurance as simple as possible</div>
  <div class="feature" style="left:106px;top:217px"><div class="ring"><span><svg style="color:var(--ink)"><use href="#i-coin"/></svg></span></div><div><h3>we've made insurance as simple as possible</h3><p>You can reduce your current residual value to a lower amount, this option will reduce</p></div></div>
  <div class="feature" style="left:429px;top:217px"><div class="ring"><span><svg style="color:var(--ink)"><use href="#i-doc"/></svg></span></div><div><h3>No agents and no commissions, so you save money.</h3><p>You can reduce your current residual value to a lower amount, this option will reduce</p></div></div>
  <div class="feature" style="left:771px;top:217px"><div class="ring"><span><svg style="color:var(--ink)"><use href="#i-bars"/></svg></span></div><div><h3>No more long meetings. Just a few clicks or a short call and you are done.</h3><p>You can reduce your current residual value to a lower amount, this option will reduce</p></div></div>
  <div class="feature" style="left:106px;top:367px"><div class="ring"><span><svg style="color:var(--ink)"><use href="#i-bars"/></svg></span></div><div><h3>so you can claim easily with a few clicks of your mobile.</h3><p>You can reduce your current residual value to a lower amount, this option will reduce</p></div></div>
  <div class="feature" style="left:429px;top:367px"><div class="ring"><span><svg style="color:var(--ink)"><use href="#i-user"/></svg></span></div><div><h3>Easy to use website so you can breeze through to compare, buy or claim.</h3><p>You can reduce your current residual value to a lower amount, this option will reduce</p></div></div>
  <div class="feature" style="left:771px;top:367px"><div class="ring"><span><svg style="color:var(--ink)"><use href="#i-screen"/></svg></span></div><div><h3>Simple language and no small print, so you know exactly what you will get every time.</h3><p>You can reduce your current residual value to a lower amount, this option will reduce</p></div></div>
  <a class="btn">Apply Online Now <span class="arr" style="color:var(--ink)"><svg><use href="#i-arrow"/></svg></span></a>
</section>

<section class="how">
  <h2 class="sec-title">How it Works on Veloraguvence?</h2>
  <p class="sec-sub">Lorem Ipsum is simply dummy text of the printing and typesetting industry. Lorem Ipsum has been the industry's standard dummy text ever since the 1500s, when an unknown printer took a galley of type and scrambled it to make a type specimen book. It has survived not only five centuries, but also the leap into electronic.</p>
  <div class="step" style="left:119px"><span class="ic"><svg style="color:var(--ink)"><use href="#i-hand"/></svg></span><div><h4>1.Complete 'Get a Quote'</h4><p>It takes less than 2 minutes to complete the form with your info to help us complete your quote.</p></div></div>
  <div class="step" style="left:450px"><span class="ic"><svg style="color:var(--ink)"><use href="#i-screen"/></svg></span><div><h4>2. We review info</h4><p>It takes less than 2 minutes to complete the form with your info to help us complete your quote.</p></div></div>
  <div class="step" style="left:777px"><span class="ic"><svg style="color:var(--ink)"><use href="#i-coin"/></svg></span><div><h4>3.You receive quotes</h4><p>It takes less than 2 minutes to complete the form with your info to help us complete your quote.</p></div></div>
  <a class="btn">Apply Online Now <span class="arr" style="color:#fff"><svg><use href="#i-arrow"/></svg></span></a>
</section>

<section class="reviews">
  <h2 class="sec-title">Here's what customers are saying about us</h2>
  <div class="rated">we were rated an average of 9/10 by 1398 of our customers &nbsp;<b>■ ReviewNest</b></div>
  <svg class="nav-arr" style="left:44px" viewBox="0 0 30 60"><path d="M24 4L6 30l18 26" fill="none" stroke="#777" stroke-width="2"/></svg>
  <svg class="nav-arr" style="left:1112px" viewBox="0 0 30 60"><path d="M6 4l18 26L6 56" fill="none" stroke="#777" stroke-width="2"/></svg>
  <div class="review" style="left:110px"><h5><i></i>Very good and Convinenet</h5><p>Mauris pharetra ornare lectus at dapibus. Donec id ex quis nisi elementum fringilla non in urna. Morbi nec orci sapien. Sed facilisis lorem vel lacinia accumsan. Aliquam viverra gravida lorem, et viverra tellus bibendum non. Phasellus vitae.</p><div class="who"><span class="av"></span><span>Selin Karaca, Moda<br>from Kadikoy, Istanbul</span></div><div class="stars"><i></i><i></i><i></i><i></i><i></i></div></div>
  <div class="review" style="left:442px"><h5><i></i>Easy to navigate websites</h5><p>Mauris pharetra ornare lectus at dapibus. Donec id ex quis nisi elementum fringilla non in urna. Morbi nec orci sapien. Sed facilisis lorem vel lacinia accumsan. Aliquam viverra gravida lorem, et viverra tellus bibendum non. Phasellus vitae.</p><div class="who"><span class="av"></span><span>Selin Karaca, Moda<br>from Kadikoy, Istanbul</span></div><div class="stars"><i></i><i></i><i></i><i></i><i></i></div></div>
  <div class="review" style="left:773px"><h5><i></i>Very good and Convinenet</h5><p>Mauris pharetra ornare lectus at dapibus. Donec id ex quis nisi elementum fringilla non in urna. Morbi nec orci sapien. Sed facilisis lorem vel lacinia accumsan. Aliquam viverra gravida lorem, et viverra tellus bibendum non. Phasellus vitae.</p><div class="who"><span class="av"></span><span>Selin Karaca, Moda<br>from Kadikoy, Istanbul</span></div><div class="stars"><i></i><i></i><i></i><i></i><i></i></div></div>
  <div class="dots"><i></i><i></i><i></i><i></i><i class="on"></i><i></i><i></i><i></i></div>
</section>

<section class="promo">
  <div class="photo" role="img" aria-label="Photo of a happy couple holding car keys beside a yellow car"></div>
  <div class="panel"></div>
  <div class="kicker">Best Rates On Car, Bike, Caravan Insurance in Veloraguvence</div>
  <h3>Buy your Vehicle from any Dealer or Private seller</h3>
  <ul><li>High approval rate</li><li>No deposit required</li><li>Pre approval in under 15 seconds</li><li>Finance approved in just a few hours</li></ul>
  <a class="btn">Apply Now <span class="arr" style="color:#fff"><svg><use href="#i-arrow"/></svg></span></a>
  <div class="seal" role="img" aria-label="Lowest price guarantee seal"></div>
</section>

<section class="partners">
  <h2 class="sec-title">Insurance Companies</h2>
  <div class="sec-sub">Turkey's top 20 insurance companies in the dozens of insurance package to offer the most convenient We help you achieve!</div>
  <div class="logos">
    <span>Kuzey Sigorta</span><span>Tarla Sigorta</span><span>Alpera</span><span>Alpera Hayat</span><span>Ovacik Sigorta</span><span>Eurona</span>
    <span>Dalga Sigorta</span><span>Dalga Emeklilik</span><span>ORVA</span><span>Marlo Sigorta</span><span>Isik Sigorta</span><span>Kumo Sigorta</span>
    <span>Grovia</span><span>Safak Sigorta</span><span>Meydan Sigorta</span><span>Hedef Sigorta</span><span>Birlik</span><span>Zirve Sigorta</span>
    <span>Pusula Direct</span><span>Ozgur</span><span>Yuvam Kredi</span><span>Marquet</span><span>Mavi Bank</span><span>Nehir</span>
  </div>
  <a class="btn">All Contracted Insurance Companies <span class="arr" style="color:#fff"><svg><use href="#i-arrow"/></svg></span></a>
</section>

<section class="stats" role="region" aria-label="Company figures over a dimmed photo of a vintage car">
  <h2 class="sec-title">Veloraguvence. How Large?</h2>
  <p class="sec-sub">We provide Turkey's first online insurance broker since 2001, as more than 3 million people, 10 million of insurance on offer. With our experienced staff, we are with you 24/7!</p>
  <div class="stat" style="left:137px"><div class="c"><svg style="color:var(--ink)"><use href="#i-cal"/></svg></div><b>12</b><small>Years Experience</small></div>
  <div class="stat" style="left:343px"><div class="c"><svg style="color:var(--ink)"><use href="#i-doc"/></svg></div><b>10K</b><small>Insurance</small></div>
  <div class="stat" style="left:524px"><div class="c"><svg style="color:var(--ink)"><use href="#i-people"/></svg></div><b>190</b><small>Happiness</small></div>
  <div class="stat" style="left:707px"><div class="c"><svg style="color:var(--ink)"><use href="#i-user"/></svg></div><b>200</b><small>Experts</small></div>
  <div class="stat" style="left:887px"><div class="c"><svg style="color:var(--ink)"><use href="#i-screen"/></svg></div><b>200</b><small>Clientes Reviews</small></div>
</section>

<section class="articles">
  <h2 class="sec-title">Be Inspired Our Ariticles</h2>
  <div class="posts">
    <article class="post"><div class="img" role="img" aria-label="Photo of two people signing insurance papers" style="background:linear-gradient(135deg,#d9d2c8,#b9aea0)"></div><div class="tag">Business Rescue</div><h6>What You Should Know About Zika Virus</h6><div class="meta">Posted by Deniz Arslan | on May 11, 2016</div><p>Lorem Ipsum is simply dummy text of the printing and typesetting industry. Lorem Ipsum has been the industry's standard dummy text ever since the 1500s, when an unknown printer took a galley.</p><span class="go"></span></article>
    <article class="post"><div class="img" role="img" aria-label="Photo of a couple reviewing documents at home" style="background:linear-gradient(135deg,#e6ddd0,#c7b9a6)"></div><div class="tag">Debt Agreements</div><h6>How to sleep less and live longer</h6><div class="meta">Posted by Deniz Arslan | on May 11, 2016</div><p>Lorem Ipsum is simply dummy text of the printing and typesetting industry. Lorem Ipsum has been the industry's standard dummy text ever since the 1500s, when an unknown printer took a galley.</p><span class="go"></span></article>
    <article class="post"><div class="img" role="img" aria-label="Photo of a couple with a laptop on a sofa" style="background:linear-gradient(135deg,#dcd5cb,#a99e91)"></div><div class="tag">Credit Monitoring</div><h6>What You Should Know About Zika Virus</h6><div class="meta">Posted by Deniz Arslan | on May 11, 2016</div><p>Lorem Ipsum is simply dummy text of the printing and typesetting industry. Lorem Ipsum has been the industry's standard dummy text ever since the 1500s, when an unknown printer took a galley.</p><span class="go"></span></article>
    <article class="post"><div class="img" role="img" aria-label="Photo of a family planning their budget" style="background:linear-gradient(135deg,#e0d7cb,#b3a594)"></div><div class="tag">Bankruptcy</div><h6>How to Choose Healthy Body Care</h6><div class="meta">Posted by Deniz Arslan | on May 11, 2016</div><p>Lorem Ipsum is simply dummy text of the printing and typesetting industry. Lorem Ipsum has been the industry's standard dummy text ever since the 1500s, when an unknown printer took a galley.</p><span class="go"></span></article>
    <article class="post"><div class="img" role="img" aria-label="Photo of a driver at the wheel" style="background:linear-gradient(135deg,#9aa3a8,#5f676b)"></div><div class="tag">Business Rescue</div><h6>What You Should Know About Zika Virus</h6><div class="meta">Posted by Deniz Arslan | on May 11, 2016</div><p>Lorem Ipsum is simply dummy text of the printing and typesetting industry. Lorem Ipsum has been the industry's standard dummy text ever since the 1500s, when an unknown printer took a galley.</p><span class="go"></span></article>
    <article class="post"><div class="img" role="img" aria-label="Photo of a smiling family outdoors" style="background:linear-gradient(135deg,#cfc8bc,#8f8577)"></div><div class="tag">Debt Agreements</div><h6>How to sleep less and live longer</h6><div class="meta">Posted by Deniz Arslan | on May 11, 2016</div><p>Lorem Ipsum is simply dummy text of the printing and typesetting industry. Lorem Ipsum has been the industry's standard dummy text ever since the 1500s, when an unknown printer took a galley.</p><span class="go"></span></article>
    <article class="post"><div class="img" role="img" aria-label="Photo of banknotes spread out" style="background:linear-gradient(135deg,#c9b48a,#8a7650)"></div><div class="tag">Credit Monitoring</div><h6>What You Should Know About Zika Virus</h6><div class="meta">Posted by Deniz Arslan | on May 11, 2016</div><p>Lorem Ipsum is simply dummy text of the printing and typesetting industry. Lorem Ipsum has been the industry's standard dummy text ever since the 1500s, when an unknown printer took a galley.</p><span class="go"></span></article>
    <article class="post"><div class="img" role="img" aria-label="Photo of stacked coins" style="background:linear-gradient(135deg,#c59b62,#7c5a30)"></div><div class="tag">Bankruptcy</div><h6>How to Choose Healthy Body Care</h6><div class="meta">Posted by Deniz Arslan | on May 11, 2016</div><p>Lorem Ipsum is simply dummy text of the printing and typesetting industry. Lorem Ipsum has been the industry's standard dummy text ever since the 1500s, when an unknown printer took a galley.</p><span class="go"></span></article>
  </div>
  <a class="more">View more Blogs <span class="arr"></span></a>
  <div class="chat">▣ CHAT WITH US ONLINE &nbsp;⌃</div>
</section>

<section class="callbar">Have more questions? Call us now: 800-555-0197</section>

<footer class="site-foot">
  <div class="brand"><span class="mark" style="background:var(--yellow)"></span><span class="name">VELORA</span></div>
  <p class="about">Lorem Ipsum is simply dummy text of the printing and typesetting industry. Lorem Ipsum has been the industry's standard dummy text ever since the 1500s, when an unknown printer took a galley of type and scrambled it to make a type book. It has survived not only five centuries.</p>
  <div class="legal" style="top:152px">Privacy and Terms of Use also agreement</div>
  <div class="socials"><i></i><i></i><i></i><i></i><i></i></div>
  <div class="fcol" style="left:394px"><h5>Quick Links</h5>Home<br>ITO Report<br>About<br>Debt Counselling<br>Debt Calculator<br>Employer Services<br>Application<br>Become An Agent</div>
  <div class="fcol" style="left:541px"><h5>Our Products</h5>Car<br>Travel<br>Medi<br>Home<br>International Health<br>Term Life<br>Commercial Car<br>Motorcycle<br>Personal Accident<br>Endowment<br>Group Insurance</div>
  <div class="fcol" style="left:700px"><h5>Support</h5>Help<br>Contact Us<br>Blog<br>FAQ<br>Website Terms of Use<br>Privacy Statement<br>Test Only</div>
  <div class="fcol" style="left:840px;width:240px"><h5>Contact Address</h5>
    <div class="row"><svg style="color:#fff"><use href="#i-pin"/></svg><span>Ardic Media Ltd, 48 Cinar Cd,<br>Alsancak, Izmir 35220</span></div>
    <div class="row"><svg style="color:#fff"><use href="#i-phone"/></svg><span>800 - 555 - 0197</span></div>
    <div class="row"><svg style="color:#fff"><use href="#i-mail"/></svg><span>info@veloraguvence.com</span></div>
    <div class="row"><svg style="color:#fff"><use href="#i-clock"/></svg><span><b style="color:#fff">OPENING TIMES</b><br>Monday – Friday 9am – 7.30pm<br>Saturdays 10am – 4pm<br>Closed Sundays and Bank Holidays</span></div>
  </div>
  <div class="subscribe"><h5>Subscribe Now</h5><div class="field"><span>Enter your Email Address</span><b><svg width="12" height="12" style="color:var(--ink)"><use href="#i-arrow"/></svg></b></div></div>
</footer>

<footer class="baseline">© 2016 by www.veloraguvence.com . All Rights Reserved<br>Terms &amp; Conditions | Privacy Policy | Complaints Procedure | Cookie Policy | Acceptable Use Policy | Press Office</footer>

</body>
</html>
```